Simple Easy - Taekwondo brochure

I have the content and an idea of the layout I want. I need it to look nice and sharp.

It's a sided 8.5x11 colored brochure

please feel free to move things around and use the images provided

my website is www.brightpathdojo.example if you need an understanding of what the business is about.

all text content is on the website. please be creative!

Target Market(s)

Mothers...must by family friendly because it's for mothers to bring their kids.

Industry/Entity Type

Martial Art

Font styles to use
Other font styles liked:
• Lato

```html
<!DOCTYPE html>
<html lang="en">
<head>
<meta charset="utf-8">
<title>Bright Path Dojo – Trifold Brochure</title>
<link href="https://fonts.googleapis.com/css2?family=Oswald:wght@500;700&family=Lato:ital,wght@0,400;0,700;0,900;1,400&display=swap" rel="stylesheet">
<style>
  :root{
    --charcoal:#343434;
    --charcoal-deep:#2b2b2b;
    --grey-light:#e4e4e4;
    --grey-mid:#c9c9c9;
    --red:#e3161b;
    --blue:#1b7fc9;
    --blue-text:#1e8fe0;
    --white:#ffffff;
    --ink:#1a1a1a;
    --offer-yellow:#fff3b0;
  }
  html,body{margin:0;padding:0;overflow:hidden;background:var(--white);}
  .brochure{position:relative;width:1200px;height:867px;overflow:hidden;background:var(--white);font-family:"Lato",sans-serif;}
  .backdrop{position:absolute;inset:0;}
  .block{position:absolute;margin:0;}

  /* Left panel */
  .bio-title{left:55px;top:24px;font-family:"Oswald",sans-serif;font-weight:500;font-size:24px;color:var(--white);letter-spacing:.3px;}
  .bio-text{left:55px;top:68px;width:270px;font-size:14px;line-height:1.32;color:var(--white);}
  .mascot-art{left:90px;top:300px;width:235px;height:165px;border-radius:18px;background:linear-gradient(135deg,#f3a64a,#fbe3c0 60%,#f7f7f7);}
  .awards-title{left:55px;top:480px;font-family:"Oswald",sans-serif;font-weight:500;font-size:23px;color:var(--white);letter-spacing:.3px;white-space:nowrap;}
  .awards-list{left:55px;top:524px;width:300px;list-style:none;padding:0;font-size:12.6px;line-height:1.3;color:var(--white);}
  .awards-list li{margin-bottom:14px;}

  /* Middle panel */
  .quote-title{left:412px;top:134px;width:394px;text-align:center;font-family:"Oswald",sans-serif;font-weight:500;font-size:20px;color:var(--white);letter-spacing:.5px;}
  .quote-text{left:440px;top:172px;width:340px;text-align:center;font-style:italic;font-size:13.6px;line-height:1.4;color:var(--white);}
  .quote-text p{margin:0 0 16px;}
  .call-title{left:412px;top:530px;width:394px;text-align:center;font-family:"Oswald",sans-serif;font-weight:700;font-size:26px;color:var(--blue-text);}
  .phone{left:412px;top:570px;width:394px;display:flex;justify-content:center;align-items:center;gap:12px;font-family:"Oswald",sans-serif;font-weight:700;font-size:30px;color:var(--ink);}
  .phone svg{width:26px;height:26px;}
  .address{left:412px;top:616px;width:394px;text-align:center;font-size:14px;line-height:1.35;color:var(--ink);font-style:normal;}
  .web{left:412px;top:676px;width:394px;text-align:center;font-weight:900;font-size:20px;color:var(--ink);}

  /* Right panel */
  .brand-name{left:860px;top:250px;width:320px;text-align:center;font-family:"Oswald",sans-serif;font-weight:700;font-size:46px;line-height:1.05;color:var(--white);}
  .tagline{left:835px;top:588px;width:300px;text-align:center;font-family:"Oswald",sans-serif;font-weight:700;font-size:38px;line-height:1.05;color:var(--ink);transform:rotate(-38deg);transform-origin:center;}
  .offer-title{left:990px;top:748px;width:210px;text-align:center;font-family:"Oswald",sans-serif;font-weight:700;font-size:32px;color:var(--offer-yellow);}
  .offer-text{left:990px;top:793px;width:210px;text-align:center;font-family:"Oswald",sans-serif;font-weight:500;font-size:20px;line-height:1.3;color:var(--offer-yellow);}
</style>
</head>
<body>
<main class="brochure">
  <svg class="backdrop" width="1200" height="867" viewBox="0 0 1200 867" aria-hidden="true">
    <polygon points="0,0 400,0 400,290 0,380" fill="var(--charcoal)"/>
    <polygon points="0,380 400,290 400,330 0,470" fill="var(--grey-light)"/>
    <polygon points="0,420 400,520 400,867 0,867" fill="var(--red)"/>
    <polygon points="290,867 400,770 400,867" fill="var(--grey-mid)"/>
    <polygon points="400,0 806,0 806,40 400,190" fill="var(--grey-light)"/>
    <rect x="412" y="128" width="394" height="372" fill="var(--charcoal-deep)"/>
    <polygon points="400,700 400,867 570,867" fill="var(--charcoal)"/>
    <polygon points="440,867 520,790 610,867" fill="var(--red)"/>
    <polygon points="690,867 806,760 806,867" fill="var(--grey-mid)"/>
    <polygon points="806,0 1200,0 1200,330 806,640" fill="var(--blue)"/>
    <polygon points="806,700 806,867 900,867" fill="var(--charcoal)"/>
    <polygon points="1200,420 1200,600 1110,520" fill="var(--charcoal)"/>
    <polygon points="840,867 1200,600 1200,867" fill="var(--red)"/>
  </svg>

  <h2 class="block bio-title">MASTER DAN</h2>
  <p class="block bio-text">Daniel Cho, (Master Dan), is the owner and head instructor at Bright Path Dojo. Master Dan is a Dan Heritage Institute-certified 3rd degree Black Belt. The Dan Heritage Institute is the overseeing authority of all Black Belts in the world, working with the International Taekwondo Union (ITU); it also oversees taekwondo in international games.</p>
  <div class="block mascot-art" role="img" aria-label="Cartoon tiger mascots in taekwondo uniforms"></div>
  <h2 class="block awards-title">AWARDS / ACHIEVEMENTS</h2>
  <ul class="block awards-list">
    <li>(under Master<br>Dan's leadership)</li>
    <li>4 National Taekwondo Alliance<br>National Championships<br>/ ITU sanctioned</li>
    <li>10 State Medalists National<br>Taekwondo State Championships /<br>ITU sanctioned</li>
    <li>12 Atlantic Collegiate Taekwondo<br>League (ACTL) Team Medals / ITU<br>sanctioned</li>
    <li>1 Atlantic Collegiate Taekwondo League (ACTL)<br>TOP DIVISION TEAM TITLES / ITU sanctioned</li>
  </ul>

  <h2 class="block quote-title">TESTIMONIAL</h2>
  <blockquote class="block quote-text">
    <p>I started taking classes with Master Dan a little over 3 years ago. As the newest member of the class, I was shy and unsure of myself.</p>
    <p>However, I quickly overcame those feelings because Master Dan is a natural teacher. Paired with his passion for the sport, his gift for teaching makes him one of the best coaches I have encountered. I have seen him work with both children and adults and his manner is unfailingly supportive and encouraging.</p>
    <p>As a teacher myself, I see how he tailors his teaching style to each student and I hope to follow his example in my classroom. I am thankful that my first experience with taekwondo has been through Master Dan's class.</p>
    <p>- Rachel T.</p>
  </blockquote>
  <p class="block call-title">Call us today !</p>
  <p class="block phone">
    <svg viewBox="0 0 24 24" aria-hidden="true"><path fill="var(--blue)" d="M6.6 10.8a15.1 15.1 0 0 0 6.6 6.6l2.2-2.2a1 1 0 0 1 1-.25 11.4 11.4 0 0 0 3.6.57 1 1 0 0 1 1 1V20a1 1 0 0 1-1 1A17 17 0 0 1 3 4a1 1 0 0 1 1-1h3.5a1 1 0 0 1 1 1c0 1.25.2 2.45.57 3.57a1 1 0 0 1-.25 1z"/></svg>
    (215) 555-0147
  </p>
  <address class="block address">Bright Path Dojo<br>2280 Maple Ridge Road<br>Oakfield, PA 19400</address>
  <p class="block web">www.brightpathdojo.example</p>

  <p class="block brand-name">BRIGHT PATH<br>DOJO</p>
  <p class="block tagline">Focus your<br>child's potential</p>
  <h2 class="block offer-title">SPECIAL OFFER</h2>
  <p class="block offer-text">50% off trial lessons<br>and get a free t-shirt!</p>
</main>
</body>
</html>
```